Lanterns Over The Quiet Meadow Waters Book Cover

Book cover for a new book titled "Lanterns Over The Quiet Meadow Waters" which will show how retirees can pay NO tax in their retirement. Would like you to use your creative inspiration to come up with a design.

Please make MEADOW WATERS the emphasis of the title.

can you show money being rescued, or freed, from taxes.

I'm trying convey the message that retirees can FREE themselves from the burden of taxes in retirement by reading this book and following the instructions. Think about a person swimming with a weight on his back, sinking him. Suddenly the weight is removed. The feeling and imagery of the load being light now

Doing MEADOW WATERS can alleviate many of unnecessary taxes which will weight retirees down. But, unfortunately, many advisors in my industry do not educate their clients on this stuff.

Not a fan of dark backgrounds, generally speaking. Lighter is good.

Remember folks, go to brindlecart. Type in Roth IRA books. what will jump out over the stuff that's already there? Thanks!

Target Market(s)

recent, or soon to be, retirees, people in their 50s and 60s, typically couples

Industry/Entity Type

Financial

Font styles to use
Serif

Colors

Designer to choose colors to be used in the design.

Requirements
Must have
• Be optimistic, sunny, happy. How you do that? I don't know, that's why I'm hiring you. This book is designed for the lay person, (average Joe and Jane)
• Put my picture on the lower back.
• My name at bottom of the cover
Nice to have
• Be nice to have the cover POP on Brindlecart because I'm competing with so many other books and thumbnails
• Maybe a kite with a dollar bill that is breaking from a ball and chain? Just an idea.
Should not have
• No guys in suits. Happy couples sitting on the beach or sailing. That stuff is in every piece of financial planning literature.
• NOT TECHNICAL. NO PIGGY BANKS Design please

```html
<!DOCTYPE html>
<html lang="en">
<head>
<meta charset="utf-8">
<title>Lanterns Over The Quiet Meadow Waters — Book Cover</title>
<link rel="stylesheet" href="https://fonts.googleapis.com/css2?family=Montserrat:wght@800&family=Open+Sans:wght@300;400&display=swap">
<style>
  :root {
    --sky: #dcecf5;
    --sky-haze: #eef5f8;
    --ink-teal: #1d4e6a;
    --title-yellow: #fbef2a;
    --title-shadow: rgba(90, 90, 70, 0.45);
    --sea-deep: #2e97b6;
    --sea-light: #5cbdd3;
    --sand-light: #e6d8bd;
    --sand-dark: #c9b38e;
    --band: #dcecf5;
  }
  * { margin: 0; padding: 0; box-sizing: border-box; }
  html, body { width: 840px; height: 1200px; overflow: hidden; background: var(--sky); }
  .cover {
    position: relative;
    width: 840px;
    height: 1200px;
    overflow: hidden;
    background: var(--sky);
  }
  .beach-scene {
    position: absolute;
    left: 0; top: 470px;
    width: 840px; height: 730px;
    background: linear-gradient(to bottom,
      var(--sky) 0px,
      var(--sky-haze) 140px,
      #f4f8f9 250px,
      #e4eff3 284px,
      var(--sea-deep) 288px,
      var(--sea-light) 360px,
      #7cc6d3 405px,
      var(--sand-dark) 412px,
      var(--sand-light) 470px,
      #dccaa8 620px,
      var(--sand-dark) 730px);
  }
  .title {
    position: absolute;
    left: 0; top: 0;
    width: 840px; height: 500px;
  }
  .title-lead {
    font-family: "Open Sans", sans-serif;
    font-weight: 400;
    font-size: 41px;
    fill: var(--ink-teal);
  }
  .title-main, .title-sub {
    font-family: "Montserrat", sans-serif;
    font-weight: 800;
    fill: var(--title-yellow);
  }
  .title-main { font-size: 262px; }
  .title-sub { font-size: 98px; }
  .author-band {
    position: absolute;
    left: 0; top: 1121px;
    width: 840px; height: 56px;
    background: var(--band);
    display: flex; align-items: center; justify-content: center;
  }
  .author-name {
    font-family: "Open Sans", sans-serif;
    font-weight: 300;
    font-size: 44px;
    letter-spacing: 0.36em;
    margin-right: -0.36em;
    color: var(--ink-teal);
    line-height: 1;
  }
</style>
</head>
<body>
  <main class="cover">
    <div class="beach-scene" role="img" aria-label="Photograph of two light blue wooden beach chairs on sand facing a calm turquoise sea under a pale sky"></div>

    <svg class="title" viewBox="0 0 840 500" width="840" height="500" aria-label="Lanterns Over The Quiet Meadow Waters">
      <defs>
        <filter id="title-drop" x="-5%" y="-5%" width="110%" height="115%">
          <feDropShadow dx="1.5" dy="2" stdDeviation="0.8" flood-color="var(--title-shadow)"/>
        </filter>
      </defs>
      <text class="title-lead" x="92" y="175">Lanterns Over The Quiet</text>
      <text class="title-main" x="88" y="384" textLength="662" lengthAdjust="spacingAndGlyphs" filter="url(#title-drop)">MEADOW</text>
      <text class="title-sub" x="88" y="478" textLength="662" lengthAdjust="spacing" filter="url(#title-drop)">WATERS</text>
    </svg>

    <div class="author-band">
      <span class="author-name">DALE WHITCOMBE</span>
    </div>
  </main>
</body>
</html>
```